"White Paper" for Brightfield Tutoring, LLC

Hi there! I'm creating a short white paper for my business that people will download from my website (not yet launched) in PDF format. I want to create this document in Word and manage/finalize the text myself. I have created a primitive Word document (using mostly filler text) that shows the elements of this White Paper, and the design elements that need to be done, including: 1) making the cover look good; 2) choosing fonts; 3) creating several design elements such as a pull quotes and a bullet "how to tell" box; 4) creating a table of contents page; 5) making the photos (included) look good - you may process and size them anyway you like, but please include these photos in the sections they are already in (and know these photos are free to use); 6) designing section headers; and a few other misc. tasks.

The deliverable back from you is a word file (can be a straight doc or a template, whichever you think best) that I will be able to modify and use myself. Of course, until I buy your design, you can post it in a form that I can see but not manipulate. But know that when I buy it, I want a Word document.

Tight turnaround for this - need it done in 2 days. Email me with questions. Thank you.

Target Market(s)

Parents of K-12 children in the USA.

Industry/Entity Type

Education

Font styles to use
Sans Serif

Colors
3276b5
b768aa
d2a4cc
85abd2

Requirements
Must have
• Clean design that projects my credibility
• Flexibility so I can change text and some elements (such as size of pull quotes and the "How to Tell" text box
• Final product must be delivered to me in a Microsoft Word file that I can modify myself

```html
<!DOCTYPE html>
<html lang="en">
<head>
<meta charset="utf-8">
<title>Quick Guide – Making the Final Decision</title>
<link href="https://fonts.googleapis.com/css2?family=Bebas+Neue&family=Roboto:wght@300;400;500&display=swap" rel="stylesheet">
<style>
:root{
  --blue:#4a94d0;
  --blue-dark:#1f6fc0;
  --violet:#b03fa6;
  --pink:#d88bd2;
  --lilac:#e8c2e6;
  --quote:#8a5a9a;
  --gray-bg:#e3e3e3;
  --gray:#b9b9b9;
  --ink:#1c1c1c;
}
*{margin:0;padding:0;box-sizing:border-box}
html,body{width:1200px;height:1162px;overflow:hidden;background:var(--gray-bg)}
body{position:relative;font-family:"Roboto",sans-serif;color:var(--ink)}
.page{position:absolute;width:385px;height:555px;background:#fff;overflow:hidden}
.page-head{height:47px;background:var(--blue);color:#fff;font-family:"Bebas Neue",sans-serif;font-weight:400;font-size:36px;letter-spacing:.5px;text-align:center;line-height:50px}
.body-copy{font-size:10px;line-height:15.6px;text-align:justify}
.body-copy p{margin-bottom:3px}
.drop::first-letter{font-size:17px;font-weight:500}
.footer{position:absolute;left:0;bottom:0;width:385px;height:18px}
.footer svg{position:absolute;left:0;top:0}
.footer-text{position:absolute;left:14px;top:1px;font-size:10px;color:#fff}
.page-no{position:absolute;right:14px;bottom:17px;font-size:11px;line-height:13px}
/* cover */
.cover-title{position:absolute;top:67px;width:100%;text-align:center;font-size:29px;font-weight:500;line-height:34px;color:var(--blue-dark)}
.cover-title em{font-style:normal;color:var(--pink)}
.portrait{position:absolute;left:77px;top:161px;width:228px;height:313px;background:radial-gradient(ellipse at 50% 30%,#d7a88f 0 18%,#b9cde6 19% 100%)}
.cover-band{position:absolute;left:0;top:474px;width:385px;height:81px;background:var(--blue)}
.cover-tab{position:absolute;left:185px;top:458px}
.cover-label{position:absolute;top:498px;width:100%;text-align:center;color:#fff;font-size:37px;font-weight:300}
/* toc */
.toc{position:absolute;left:22px;top:62px;width:342px;list-style:none}
.toc li{display:flex;align-items:center;height:30.8px;font-size:12.3px;font-weight:500;color:var(--blue-dark)}
.toc .label{width:132px}
.toc .dots{width:155px;border-bottom:1.5px dotted var(--blue-dark);height:6px;margin-right:auto}
.toc .num{width:24px;text-align:right;font-weight:400}
.section-title{font-family:"Bebas Neue",sans-serif;font-size:24px;line-height:29px;color:var(--violet);text-align:center}
.callout{background:var(--lilac);border-radius:20px;padding:5px}
.callout-inner{border:1px dashed #fff;border-radius:16px;padding:8px 18px}
/* pull quote */
.pull-quote{float:left;width:136px;margin:2px 9px 0 0;padding-left:26px;font-size:14.4px;line-height:24px;text-align:left;position:relative}
.q-mark{font-family:"Bebas Neue",sans-serif;color:var(--quote);line-height:1}
.q-open{position:absolute;left:0;top:0;font-size:34px}
.q-close{font-size:28px;vertical-align:-8px}
.checks{list-style:none;margin:6px 0 6px 4px}
.checks li{position:relative;padding-left:18px;margin-bottom:7px;text-align:left}
.checks svg{position:absolute;left:0;top:3px}
.tips{list-style:none;font-size:9.3px;line-height:14px}
.tips li{position:relative;padding-left:14px;margin:1px 0}
.tips li::before{content:"✥";position:absolute;left:0;font-size:9px}
.chalkboard{float:right;width:159px;height:107px;margin:4px 0 2px 10px;border:2px solid var(--pink);background:linear-gradient(#1d2126 0 62%,#8b6a50 62% 100%)}
</style>
</head>
<body>

<section class="page" style="left:19px;top:19px">
  <h1 class="page-head">Making the Final Decision</h1>
  <div class="cover-title">About which <em>K-12 school</em><br><em>my child</em> should attend</div>
  <div class="portrait" role="img" aria-label="Portrait photo of the author in a light blue shirt, arms crossed"></div>
  <svg class="cover-tab" width="110" height="17"><polygon points="0,16 13,0 105,0 92,16" fill="var(--gray)"/></svg>
  <div class="cover-band"></div>
  <div class="cover-label">QUICK GUIDE</div>
</section>

<section class="page" style="left:411px;top:19px">
  <h2 class="page-head">Table of Contents</h2>
  <ul class="toc">
    <li><span class="label">Introduction</span><span class="dots"></span><span class="num">3</span></li>
    <li><span class="label">Teaching</span><span class="dots"></span><span class="num">4</span></li>
    <li><span class="label">Program</span><span class="dots"></span><span class="num">6</span></li>
    <li><span class="label">Culture</span><span class="dots"></span><span class="num">8</span></li>
    <li><span class="label">Where graduates go</span><span class="dots"></span><span class="num">10</span></li>
    <li><span class="label">Your family’s needs</span><span class="dots"></span><span class="num">11</span></li>
    <li><span class="label">Making Tradeoffs</span><span class="dots"></span><span class="num">12</span></li>
  </ul>
  <div class="section-title" style="position:absolute;top:303px;width:100%">“About Dan”</div>
  <div class="callout body-copy" style="position:absolute;left:9px;top:338px;width:366px;font-size:9.4px">
    <div class="callout-inner">Lorem ipsum dolor sit amet nam feugiat scelerisque erat. Eros quis nunc.Aliquam pellentesque posuere vulputate rhoncus duis. Donec iaculis excepturi nostra wisi velit ultrices vel vel. Ultrices eu eu. Quam vitae felis.Platea feugiat nulla.Malesuada dui aut. Ullamcorper adipiscing tincidunt duis in maecenas in praesent est. Nulla volutpat sem justo rutrum leo. Aliquet posuere class luctus est in proin risus praesent nam aenean eu. Risus blandit pede vestibulum eget tellus metus pellentesque dui. Lectus aliquet diam. Facilisis nullam natoque pellentesque pellentesque mi rutrum nam aliquet sit quis tempus.</div>
  </div>
  <div class="page-no">Page No : 02</div>
  <div class="footer">
    <svg width="385" height="18"><polygon points="0,0 270,0 278,14 0,14" fill="var(--blue)"/><polygon points="278,4 385,4 385,18 286,18" fill="var(--gray)"/></svg>
    <span class="footer-text">“Copyright 2017 Brightfield Tutoring, LLC”</span>
  </div>
</section>

<section class="page" style="left:803px;top:19px">
  <h2 class="page-head">Introduction</h2>
  <div class="body-copy" style="position:absolute;left:15px;top:62px;width:356px">
    <div style="display:flex;gap:28px">
      <p class="drop" style="flex:1">Lorem ipsum dolor sit amet nam feugiat scelerisque erat. Eros quis nunc.Aliquam pellentesque posuere vulputate rhoncus duis. Donec iaculis excepturi nostra wisi velit ultrices vel vel. Ultrices eu eu. Lorem ipsum dolor sit amet nam feugiat scelerisque erat. Eros quis nunc.Aliquam pellentesque posuere vulputate rhoncus duis. Donec iaculis excepturi nostra wisi velit ultrices vel vel. Ultrices eu eu.</p>
      <p class="drop" style="flex:1">Lorem ipsum dolor sit amet nam feugiat scelerisque erat. Eros quis nunc.Aliquam pellentesque posuere vulputate rhoncus duis. Donec iaculis excepturi nostra wisi velit ultrices vel vel. Ultrices eu eu. Lorem ipsum dolor sit amet nam feugiat scelerisque erat. Eros quis nunc.Aliquam pellentesque posuere vulputate rhoncus duis. Donec iaculis excepturi nostra wisi velit ultrices vel vel. Ultrices eu eu.</p>
    </div>
    <p class="drop" style="margin-top:3px">Habitasse risus pellentesque lorem integer egestas orci viverra tellus. Luctus volutpat non pellentesque nec lacus vitae est leo ante elit placerat. Metus magna posuere porttitor magna nulla expedita varius turpis.Erat vitae nulla.Suscipit volutpat consequat.Lorem porta amet.In in turpis.Vestibulum dictum diam. Netus hendrerit nibh. Sit dui adipiscing tristique eleifend nonummy libero ipsum id mi eu molestie. Pede et tellus massa ac sit. Nullam sit felis facilisis morbi rutrum. Ac hendrerit duis cursus arcu nulla. Nec praesent est wisi dui amet. Urna quam suscipit.Et ac in. Ante eros mollis. Blandit commodo vel. Ante enim sagittis. Tellus mattis at phasellus sed non. Quis mus augue.Ut aenean libero at etiam adipiscing. Ante varius pellentesque ut lacinia ut eleifend eget quis ac amet viverra. Euismod neque laoreet placerat donec turpis.Adipiscing curabitur rhoncus.Justo mi vel vitae duis ultrices. Orci purus adipiscing. Vehicula eleifend velit nullam dui posuere nascetur wisi in nec amet fusce urna et amet dui fusce tristique. Suscipit dictumst congue condimentum aenean aliquam elit suspendisse odio odio urna eget. Nec sapien justo netus viverra et.</p>
  </div>
  <div class="page-no">Page No : 03</div>
  <div class="footer">
    <svg width="385" height="18"><polygon points="0,0 270,0 278,14 0,14" fill="var(--blue)"/><polygon points="278,4 385,4 385,18 286,18" fill="var(--gray)"/></svg>
    <span class="footer-text">www.pickabrightschool.com</span>
  </div>
</section>

<section class="page" style="left:211px;top:587px">
  <h2 class="page-head">Teaching</h2>
  <div class="body-copy" style="position:absolute;left:15px;top:54px;width:355px">
    <p class="drop">Lorem ipsum dolor. Sit amet turpis. Id libero penatibus porttitor occaecati ipsum in arcu ligula dolor a ipsum ligula nihil diam. Turpis justo morbi in in placerat. Dui donec varius risus in arcu montes mauris commodo. At nibh ut elit non porttitor non ac duis. Eget odio turpis cursus vivamus velit. Mauris proin nec consequatur id arcu aliquam faucibus maecenas. Sem quam vel praesent nullam bibendum quam imperdiet sem. Nec vitae libero sollicitudin nullam eu. Wisi cursus convallis.Integer curabitur nullam. Proin leo mollis. Facilisis amet vehicula.Venenatis consequat justo.</p>
    <ul class="checks">
      <li><svg width="11" height="11" viewBox="0 0 11 11"><rect x="1" y="2" width="8" height="8" fill="none" stroke="#333"/><path d="M2.5 5.5l2 2L10 1.5" fill="none" stroke="#333" stroke-width="1.4"/></svg>Vitae non velit. Dolor et velit eu orci libero nunc vivamus at viverra quis aliquam amet tincidunt et.</li>
      <li><svg width="11" height="11" viewBox="0 0 11 11"><rect x="1" y="2" width="8" height="8" fill="none" stroke="#333"/><path d="M2.5 5.5l2 2L10 1.5" fill="none" stroke="#333" stroke-width="1.4"/></svg>Sed porta euismod ipsum suspendisse nullam. Enim ut arcu. Lacus elementum eros neque nullam suspendisse.</li>
      <li><svg width="11" height="11" viewBox="0 0 11 11"><rect x="1" y="2" width="8" height="8" fill="none" stroke="#333"/><path d="M2.5 5.5l2 2L10 1.5" fill="none" stroke="#333" stroke-width="1.4"/></svg>Metus massa ligula. Mi pellentesque habitant diam in justo bibendum et vel. Maecenas sunt urna.</li>
    </ul>
    <p class="drop">Lectus enim venenatis.Elit vestibulum aenean. Lectus vitae scelerisque et pellentesque donec. Purus ut turpis.Augue wisi praesent.Nulla ridiculus id sapien ut nullam sapien commodo in.Euismod porta nibh. Anim pharetra massa vulputate velit arcu. Reprehenderit augue inceptos purus class ipsum omnis ipsum nam</p>
    <div class="chalkboard" role="img" aria-label="Photo of a chalkboard reading ABC with a stack of books and chalk"></div>
    <p class="drop">Lorem ipsum dolor. Sit amet turpis. Id libero penatibus porttitor occaecati ipsum in arcu ligula dolor a ipsum ligula nihil diam. Turpis justo morbi in in placerat. Dui donec varius risus in arcu montes mauris commodo. At nibh ut elit non porttitor non ac duis. Eget odio turpis cursus vivamus velit. Mauris proin nec consequatur id arcu aliquam faucibus maecenas. Sem quam</p>
  </div>
  <div class="page-no">Page No : 04</div>
  <div class="footer">
    <svg width="385" height="18"><polygon points="0,0 270,0 278,14 0,14" fill="var(--blue)"/><polygon points="278,4 385,4 385,18 286,18" fill="var(--gray)"/></svg>
    <span class="footer-text">www.pickabrightschool.com</span>
  </div>
</section>

<section class="page" style="left:611px;top:587px">
  <h2 class="page-head">Teaching</h2>
  <div class="body-copy" style="position:absolute;left:15px;top:52px;width:355px">
    <p>vel praesent nullam bibendum quam imperdiet sem. Nec vitae libero sollicitudin nullam eu. Wisi cursus convallis.Integer curabitur nullam. Proin leo mollis. Facilisis amet vehicula.Venenatis consequat justo.</p>
    <blockquote class="pull-quote"><span class="q-mark q-open">“</span>Lorem ipsum dolor sit amet, consectetur adipiscing elit.Vestibulum sit amet nulla sit amet ipsum. <span class="q-mark q-close">”</span></blockquote>
    <p class="drop">Lorem ipsum dolor. Sit amet turpis. Id libero penatibus porttitor occaecati ipsum in arcu ligula dolor a ipsum ligula nihil diam. Turpis justo morbi in in placerat. Dui donec varius risus in arcu montes mauris commodo. At nibh ut elit non porttitor non ac duis. Eget odio turpis cursus vivamus velit. Mauris proin nec consequatur id arcu aliquam faucibus maecenas. Sem quam vel praesent nullam bibendum quam imperdiet sem. Nec vitae libero sollicitudin nullam eu. Wisi cursus convallis.Integer curabitur nullam. Proin leo mollis. Facilisis amet vehicula.Venenatis consequat justo.</p>
    <p style="clear:both">Sem quam vel praesent nullam bibendum quam imperdiet sem. Nec vitae libero sollicitudin nullam eu. Wisi cursus convallis.Integer curabitur nullam. Proin leo mollis. Facilisis amet vehicula.Venenatis consequat justo.</p>
  </div>
  <div class="section-title" style="position:absolute;top:379px;width:100%">“How You Can Tell”</div>
  <div class="callout" style="position:absolute;left:10px;top:409px;width:366px">
    <div class="callout-inner" style="padding:4px 12px">
      <ul class="tips">
        <li>Integer curabitur nullam. Proin leo mollis. Facilisis amet vehicula. Venenatis consequat justo.</li>
        <li>Integer curabitur nullam. Proin leo mollis. Facilisis amet vehicula. Venenatis consequat justo.</li>
        <li>Integer curabitur nullam. Proin leo mollis. Facilisis amet vehicula. Venenatis consequat justo.</li>
      </ul>
    </div>
  </div>
  <div class="page-no">Page No : 05</div>
  <div class="footer">
    <svg width="385" height="18"><polygon points="0,0 270,0 278,14 0,14" fill="var(--blue)"/><polygon points="278,4 385,4 385,18 286,18" fill="var(--gray)"/></svg>
    <span class="footer-text">www.pickabrightschool.com</span>
  </div>
</section>

</body>
</html>
```